Design of a promotional offer flyer required to promote low-cost websites to 1-man band businesses

I want a flyer designed - either a double-sided A5 flyer or even A4 folded into a third double-sided. The flyer is to showcase a new service - low-cost websites for 1-man-band businesses, business startups and tradesmen in England. Look at the copy, find some pix and let me know! Flyer will be printed and used as an image on my website too. Pix could be related to some of the target groups. We need to stress the simple message that websites start from £5 per week and this is an-all-in-one fee.

Target Market(s)

Tradesmen, business start ups and 1-man band businesses that want a website

Industry/Entity Type

Small Business

Contact Information for Business Card

All contact details and name of business to be confirmed shortly

Font styles to use
Serif

Requirements
Must have
• Basic messages from copy for flyer i.e. websites from £5 per week and what each client gets for that price to be included on the business card! Please read copy for the flyer.
Nice to have
• Nice background image or series of small images relevant to the target audience. Again, see list of targets from copy for flyer.
Should not have
• I don't want exact or similar design to my main business Blue Anchor Marketing. The new flyer and business card should be a different and distinct branding to that of Blue Anchor Marketing. Aimed at a more economical style, whilst looking professional, but relevant to the target audiences.

```html
<!DOCTYPE html>
<html lang="en">
<head>
<meta charset="utf-8">
<title>Low-cost websites flyer</title>
<link href="https://fonts.googleapis.com/css2?family=League+Gothic&family=Mulish:wght@400;700;800&display=swap" rel="stylesheet">
<style>
:root{
  --yellow:#f2b01e;
  --yellow-light:#f7c63a;
  --charcoal:#4a4a4b;
  --charcoal-dark:#3a3a3b;
  --ink:#2d2d2d;
  --text:#3c3c3c;
  --paper:#ececec;
  --paper-dark:#d9d9d9;
  --accent:#e2245a;
}
*{margin:0;padding:0;box-sizing:border-box}
html,body{width:1200px;height:848px;overflow:hidden;background:#fff}
.canvas{position:relative;width:1200px;height:848px;font-family:"Mulish",sans-serif;color:var(--text)}
.page{position:absolute;top:0;height:848px;overflow:hidden;
  background:radial-gradient(ellipse at 50% 40%,#f6f6f6 0%,var(--paper) 55%,var(--paper-dark) 100%)}
.page--front{left:0;width:598px}
.page--back{left:602px;width:598px}
.shapes{position:absolute;inset:0}
.display{font-family:"League Gothic",sans-serif;text-transform:uppercase;line-height:1;position:absolute;white-space:nowrap}
.devices{position:absolute;border-radius:6px;
  background:linear-gradient(135deg,#2f2f31 0%,#6b6d70 45%,#d7dadc 70%,#b7bbbf 100%);opacity:.92}
.tick{position:absolute}
/* front headline */
.headline-1{left:170px;top:120px;font-size:36px;color:#fff}
.headline-2{left:170px;top:152px;font-size:48px;color:#fff}
.headline-3{left:343px;top:197px;font-size:33px;color:var(--yellow)}
/* tagline bands */
.tagline{position:absolute;left:0;top:500px;width:598px;transform:rotate(-1deg)}
.band{position:absolute;font-family:"League Gothic",sans-serif;text-transform:uppercase;font-size:33px;line-height:38px;padding:2px 10px;white-space:nowrap}
.band--dark{background:var(--charcoal-dark);color:#fff}
.band--yellow{background:var(--yellow);color:var(--ink)}
.band-1{left:38px;top:4px}
.band-2{left:50px;top:44px}
.band-3{left:118px;top:84px}
.band-3 .highlight{color:var(--yellow)}
/* lists */
.list-title{position:absolute;font-family:"League Gothic",sans-serif;font-size:31px;color:var(--yellow);padding-left:8px;border-left:1px solid #777;line-height:30px;text-transform:uppercase;white-space:nowrap}
.underline{position:absolute;height:1px;background:#777}
.underline::after{content:"";position:absolute;right:-1px;top:-3px;border-left:6px solid #777;border-top:3.5px solid transparent;border-bottom:3.5px solid transparent}
.list{position:absolute;list-style:none;font-size:12px;line-height:13px}
.list li{position:relative;padding-left:16px;margin-bottom:3.8px}
.list li::before{content:"";position:absolute;left:0;top:5px;width:7px;height:2px;background:var(--yellow)}
.list li::after{content:"";position:absolute;left:5px;top:3px;border-left:4px solid var(--yellow);border-top:3px solid transparent;border-bottom:3px solid transparent}
.web-icon{position:absolute;left:40px;top:730px}
.footer-url{position:absolute;left:374px;top:813px;font-size:19px;letter-spacing:.5px;color:#555}
.footer-url b{font-weight:400;color:#333}
/* back */
.headline-4{left:193px;top:62px;font-size:38px;color:#fff}
.headline-5{left:191px;top:88px;font-size:88px;color:#fff}
.benefits{position:absolute;left:44px;top:423px;width:540px;list-style:none;font-size:11.6px;line-height:12.6px;color:var(--ink)}
.benefits li{position:relative;padding-left:16px;margin-bottom:5.6px}
.benefits li::before{content:"";position:absolute;left:0;top:5px;width:7px;height:2px;background:var(--yellow)}
.benefits li::after{content:"";position:absolute;left:5px;top:3px;border-left:4px solid var(--yellow);border-top:3px solid transparent;border-bottom:3px solid transparent}
.price-box{position:absolute;left:30px;top:643px;width:312px;min-height:40px;background:var(--yellow);font-size:10.6px;line-height:12.6px;color:var(--ink);padding:7px 10px 7px 12px}
.phone{position:absolute;left:59px;top:695px;font-size:32px;font-weight:800;letter-spacing:1.5px;color:var(--ink)}
.contact{position:absolute;left:59px;font-size:20.5px;color:#333;letter-spacing:.3px}
.contact span{color:#888}
.contact-email{top:735px}
.contact-web{top:757px}
.contact-icon{position:absolute;left:36px}
.cta{position:absolute;left:34px;top:801px;font-size:17px;font-weight:800;color:var(--ink)}
.promo-text{position:absolute;left:350px;top:704px;width:235px;font-size:11.6px;line-height:12.6px;color:var(--ink)}
.normal-cost{position:absolute;left:350px;top:749px;font-size:15.5px;color:var(--ink)}
.terms{position:absolute;left:350px;top:803px;font-size:11.2px;line-height:12.6px;color:var(--ink)}
</style>
</head>
<body>
<div class="canvas">

  <section class="page page--front">
    <svg class="shapes" width="598" height="848" viewBox="0 0 598 848">
      <polygon points="205,0 268,0 58,250 0,250 0,228" fill="var(--yellow)"/>
      <polygon points="598,368 598,422 0,740 0,688" fill="var(--yellow)"/>
      <polygon points="24,250 498,250 552,376 78,376" fill="var(--charcoal-dark)"/>
      <polygon points="24,250 150,235 160,252" fill="var(--yellow)"/>
      <polygon points="118,108 420,108 478,240 150,240 108,236" fill="var(--charcoal)"/>
    </svg>
    <div class="display headline-1">Want a website</div>
    <div class="display headline-2">without it costing</div>
    <div class="display headline-3">the earth?</div>

    <div class="devices" style="left:36px;top:288px;width:494px;height:188px" role="img" aria-label="Phone, tablet and laptop showing a responsive website with pink arrows between them"></div>
    <svg class="tick" style="left:492px;top:372px" width="60" height="78" viewBox="0 0 60 78">
      <path d="M4 48 L22 72 L56 4" fill="none" stroke="var(--accent)" stroke-width="7" stroke-linecap="round" stroke-linejoin="round"/>
    </svg>

    <div class="tagline">
      <div class="band band--dark band-1">Professionally-designed websites for tradesmen</div>
      <div class="band band--yellow band-2">business start-ups and 1-man bands from only</div>
      <div class="band band--dark band-3">£5 <span class="highlight">per week and no upfront costs!</span></div>
    </div>

    <div class="list-title" style="left:183px;top:646px">Suitable for</div>
    <div class="underline" style="left:183px;top:678px;width:56px"></div>
    <ul class="list" style="left:194px;top:688px">
      <li>Plumbers</li><li>Electricians</li><li>Roofers</li><li>Builders</li>
      <li>Painters</li><li>Decorators</li><li>Joiners</li><li>Business Start-ups</li>
    </ul>

    <div class="list-title" style="left:349px;top:646px">1-man bands such as</div>
    <div class="underline" style="left:349px;top:678px;width:56px"></div>
    <ul class="list" style="left:360px;top:688px;width:110px">
      <li>Hairdressers</li><li>Photographers</li><li>Fitness Instructors</li>
      <li>Window Cleaners</li><li>Beauticians</li>
    </ul>
    <ul class="list" style="left:475px;top:688px;width:110px">
      <li>Gardeners</li><li>Odd Job Men</li><li>Wheelie Bin Cleaners</li>
      <li>IFAS or Self employed Consultants</li>
    </ul>

    <svg class="web-icon" width="110" height="80" viewBox="0 0 110 80" opacity=".35">
      <rect x="4" y="14" width="78" height="48" rx="4" fill="none" stroke="#777" stroke-width="3"/>
      <rect x="36" y="62" width="14" height="8" fill="#777"/>
      <rect x="26" y="70" width="34" height="4" fill="#777"/>
      <text x="12" y="47" font-family="Mulish,sans-serif" font-weight="800" font-size="17" fill="#777">www</text>
      <circle cx="88" cy="20" r="12" fill="none" stroke="#777" stroke-width="5" stroke-dasharray="4 3"/>
      <circle cx="88" cy="20" r="5" fill="#777"/>
    </svg>
    <div class="footer-url">www.<b>sitehaven</b>.com</div>
  </section>

  <section class="page page--back">
    <svg class="shapes" width="598" height="848" viewBox="0 0 598 848">
      <polygon points="265,0 330,0 240,140 160,175" fill="var(--yellow)"/>
      <polygon points="28,188 498,188 570,345 60,345" fill="var(--charcoal-dark)"/>
      <polygon points="28,188 140,178 150,192" fill="var(--yellow)"/>
      <polygon points="120,45 430,45 485,175 140,175 100,170" fill="var(--charcoal)"/>
    </svg>
    <div class="display headline-4">Here's what</div>
    <div class="display headline-5">You get</div>

    <div class="devices" style="left:64px;top:230px;width:462px;height:170px" role="img" aria-label="Phone, tablet and laptop showing a responsive website with pink arrows between them"></div>
    <svg class="tick" style="left:510px;top:305px" width="50" height="66" viewBox="0 0 50 66">
      <path d="M4 40 L18 60 L46 4" fill="none" stroke="var(--accent)" stroke-width="6" stroke-linecap="round" stroke-linejoin="round"/>
    </svg>

    <ul class="benefits">
      <li>Professionally-designed 1-page or 5-page website (Home, About Us, Services, Contact Us, News)</li>
      <li>Responsive design that displays properly on mobiles and tablets</li>
      <li>On-going changes and updates</li>
      <li>All text written for you</li>
      <li>Photographs (Royalty-free stock images)</li>
      <li>Professional email addresses e.g. info@<b>tradesmith</b>.co.uk, sales@<b>tradesmith</b>.co.uk and yourname@<b>tradesmith</b>.co.uk. We'll even set up these email addresses on your PC and laptop!</li>
      <li>Links to your social media accounts</li>
      <li>Up to 2 hours' changes each month to content, pix, and adding new pages</li>
      <li>Professional hosting for your website and email</li>
      <li><b>No upfront cost!</b> Just weekly, monthly or annual invoice - <b>you choose!</b></li>
    </ul>

    <div class="price-box">For an-all-in fee from only <b>£5 per</b> week for a 1-page<br>website or <b>£10 per</b> week for a 5-page website.</div>

    <svg class="contact-icon" style="top:705px" width="14" height="22" viewBox="0 0 14 22"><rect x="2" y="1" width="10" height="20" rx="2" fill="var(--yellow)"/><rect x="4" y="4" width="6" height="10" fill="#fff"/></svg>
    <div class="phone">0123 456 789</div>
    <svg class="contact-icon" style="top:743px" width="16" height="12" viewBox="0 0 16 12"><rect width="16" height="12" fill="var(--yellow)"/><path d="M0 0 L8 7 L16 0" fill="none" stroke="#fff" stroke-width="1.5"/></svg>
    <div class="contact contact-email"><span>info@</span>sitehaven.com</div>
    <svg class="contact-icon" style="top:764px" width="16" height="16" viewBox="0 0 16 16"><circle cx="8" cy="8" r="7" fill="none" stroke="var(--yellow)" stroke-width="1.6"/><ellipse cx="8" cy="8" rx="3" ry="7" fill="none" stroke="var(--yellow)" stroke-width="1.2"/><line x1="1" y1="8" x2="15" y2="8" stroke="var(--yellow)" stroke-width="1.2"/></svg>
    <div class="contact contact-web"><span>www.</span>sitehaven.com</div>

    <div class="underline" style="left:34px;top:792px;width:522px"></div>
    <div class="cta">For further information or to order.</div>

    <div class="list-title" style="left:352px;top:646px">Promotional offer</div>
    <div class="underline" style="left:352px;top:678px;width:60px"></div>
    <div class="promo-text">Order your new 5-page website before ............ and we'll set up a Chatterbook Page for FREE.</div>
    <div class="normal-cost">NORMAL COST: <b>£97 PLUS VAT!</b></div>
    <div class="underline" style="left:350px;top:792px;width:60px"></div>
    <div class="terms">Full terms and conditions<br>at www.<b>sitehaven</b>.com All fees plus VAT.</div>
  </section>

</div>
</body>
</html>
```